Regenerative Medicine Brochure

I want a clean modern bi-fold or tri-fold brochure. We offer non-surgical joint repair for knees, shoulders, and hips. We have many services available including regenerative medicine including stem cell allograft, palatelet rich plasma, prolotherapy, triggerpoint injection, chiropractic and rehab therapies. We are a modern multidisciplinary clinic in coastal California. My logo is already complete and is a vibrant green color. I prefer lots of white space with some areas for service description and what conditions may benefit from the services. Design should convey modern treatments, upscale office and practice, and our target audience is older adults who want to maintain an active pain-free lifestyle.

Target Market(s)

Sports injuries, athletes, seniors who are active, knee pain, shoulder pain, arthritis.

Industry/Entity Type

Alternative Medicine

Font styles to use
Serif

Colors
9bcb3c

Requirements
Must have
• Small white space where we can write date, time, location of next event/class. Colors in brochure to coordinate with logo colors provided.

```html
<!DOCTYPE html>
<html lang="en">
<head>
<meta charset="utf-8">
<title>Coastline Spine &amp; Joint – Regenerative Medicine Brochure</title>
<link rel="stylesheet" href="https://fonts.googleapis.com/css2?family=Oswald:wght@500;600&family=Roboto:wght@400;500;700&family=Arimo:wght@400;700&display=swap">
<style>
  :root {
    --lime: #9bcb3c;
    --lime-deep: #7fb02a;
    --ink: #1c2a2b;
    --ink-soft: #2d3b3b;
    --grey: #4a4f51;
    --white: #ffffff;
    --photo-dark: #1f3a12;
    --photo-mid: #4c8a1e;
    --photo-light: #a6d84a;
  }
  * { margin: 0; padding: 0; box-sizing: border-box; }
  html, body { width: 1200px; height: 927px; overflow: hidden; background: var(--white); }
  .brochure { position: relative; width: 1200px; height: 927px; overflow: hidden; background: var(--white); }
  .artwork { position: absolute; inset: 0; }

  /* Left panel */
  .info-panel { position: absolute; left: 0; top: 0; width: 398px; height: 927px; }
  .info-panel h2 {
    position: absolute; left: 28px; top: 390px; width: 350px;
    font-family: "Oswald", sans-serif; font-weight: 600; font-size: 33px; line-height: 40px;
    color: var(--ink); text-transform: uppercase; letter-spacing: 0.2px;
  }
  .info-panel .body {
    position: absolute; left: 28px; top: 484px; width: 352px;
    font-family: "Arimo", sans-serif; font-size: 18.6px; line-height: 22.6px; color: var(--ink-soft);
  }
  .info-panel .body p + p { margin-top: 22px; }
  .event-box {
    position: absolute; left: 28px; top: 834px; width: 352px; height: 66px;
    border: 2px solid var(--lime); background: var(--white);
    padding: 7px 12px;
    font-family: "Arimo", sans-serif; font-size: 14px; line-height: 17px; color: var(--ink-soft);
  }
  .event-box .event-title { font-weight: 700; color: var(--ink); text-transform: uppercase; letter-spacing: 0.5px; }
  .event-box .event-fields { display: flex; gap: 18px; margin-top: 14px; }
  .event-box .event-fields span { flex: 1; border-bottom: 1px solid var(--grey); padding-bottom: 1px; }

  /* Middle panel */
  .contact-panel { position: absolute; left: 398px; top: 0; width: 402px; height: 927px; }
  .contact-header {
    position: absolute; left: 0; top: 0; width: 402px; height: 159px; background: var(--ink);
    display: flex; align-items: center; justify-content: center; text-align: center;
    font-family: "Roboto", sans-serif; font-weight: 500; font-size: 29px; line-height: 37px; color: var(--lime);
    padding-bottom: 4px;
  }
  .contact-item { position: absolute; left: 0; width: 402px; text-align: center; }
  .contact-item .icon { display: block; margin: 0 auto; width: 56px; height: 56px; }
  .contact-item .label {
    display: block; margin-top: 9px;
    font-family: "Roboto", sans-serif; font-weight: 700; font-size: 20px; color: var(--ink);
  }
  .contact-web { top: 174px; }
  .contact-mail { top: 272px; }
  .contact-phone { top: 370px; }
  .services {
    position: absolute; left: 0; top: 470px; width: 402px; text-align: center;
    font-family: "Roboto", sans-serif; font-size: 14.5px; line-height: 18px; color: var(--ink);
  }
  .services h3 { font-size: 15px; font-weight: 700; text-transform: uppercase; letter-spacing: 0.8px; margin-bottom: 1px; }
  .services li { list-style: none; font-weight: 500; }

  /* Right panel */
  .cover-panel { position: absolute; left: 800px; top: 0; width: 400px; height: 927px; }
  .brand-mark {
    position: absolute; left: 40px; top: 52px; width: 320px; height: 120px;
    display: flex; align-items: center; justify-content: center; gap: 16px;
  }
  .brand-mark .brand-square { width: 46px; height: 46px; background: var(--lime); flex: none; }
  .brand-mark .brand-name {
    font-family: "Oswald", sans-serif; font-weight: 500; font-size: 34px; line-height: 38px;
    color: var(--lime-deep); text-transform: uppercase;
  }
  .cover-panel h1 {
    position: absolute; left: 0; top: 196px; width: 400px; text-align: center;
    font-family: "Oswald", sans-serif; font-weight: 500; font-size: 41px; line-height: 46px;
    color: var(--ink); text-transform: uppercase;
  }
  .cover-panel .intro {
    position: absolute; left: 24px; top: 342px; width: 352px; text-align: center;
    font-family: "Arimo", sans-serif; font-size: 19.4px; line-height: 27px; color: var(--grey);
  }
</style>
</head>
<body>
<div class="brochure">

  <svg class="artwork" width="1200" height="927" viewBox="0 0 1200 927">
    <defs>
      <radialGradient id="photoGlow" cx="0.45" cy="0.45" r="0.7">
        <stop offset="0" stop-color="var(--photo-light)"/>
        <stop offset="0.45" stop-color="var(--photo-mid)"/>
        <stop offset="1" stop-color="var(--photo-dark)"/>
      </radialGradient>
      <clipPath id="leftPanelClip"><rect x="0" y="0" width="398" height="927"/></clipPath>
      <clipPath id="lowerClip"><rect x="398" y="0" width="802" height="927"/></clipPath>
    </defs>

    <rect class="contact-field" x="398" y="0" width="402" height="927" fill="var(--lime)"/>
    <rect class="cover-frame" x="806" y="12" width="383" height="900" fill="none" stroke="var(--lime)" stroke-width="2.5"/>
    <path class="info-frame" d="M12 340 V914 H398" fill="none" stroke="var(--lime)" stroke-width="2.5"/>

    <g clip-path="url(#leftPanelClip)">
      <ellipse cx="165" cy="140" rx="229" ry="219" fill="var(--white)"/>
      <ellipse cx="165" cy="140" rx="225" ry="215" fill="url(#photoGlow)"
               role="img" aria-label="X-ray style image of a back and glowing spine in green tones"/>
    </g>

    <g clip-path="url(#lowerClip)">
      <ellipse cx="970" cy="1150" rx="646" ry="676" fill="var(--white)"/>
      <ellipse cx="970" cy="1150" rx="640" ry="670" fill="url(#photoGlow)"
               role="img" aria-label="X-ray style image of a spine and a knee joint in green tones"/>
    </g>
  </svg>

  <section class="info-panel">
    <h2>What is<br>Regenerative Medicine</h2>
    <div class="body">
      <p>Regenerative medicine is a form of biotechnology that involves injecting regenerative medicine products into injured tissues to help your body repair damage. Regenerative medicine uses tissue engineering techniques to repair muscles, ligaments, cartilage, and tendons damaged by injuries, overuse, and osteoarthritis.</p>
      <p>After you're injection with the amniotic allograft serum, the growth factors trigger repair at the site of injection. Over the course of the next several weeks, cells grow and multiply forming new tissue.</p>
    </div>
    <div class="event-box">
      <div class="event-title">Next Event / Class</div>
      <div class="event-fields"><span>Date:</span><span>Time:</span><span>Location:</span></div>
    </div>
  </section>

  <section class="contact-panel">
    <div class="contact-header">To learn more, schedule a<br>consultation online<br>or by phone today</div>

    <div class="contact-item contact-web">
      <svg class="icon" viewBox="0 0 60 60" aria-hidden="true">
        <circle cx="30" cy="30" r="29" fill="var(--ink)"/>
        <g fill="none" stroke="var(--lime)" stroke-width="2.4">
          <circle cx="30" cy="30" r="14"/>
          <ellipse cx="30" cy="30" rx="6" ry="14"/>
          <line x1="16" y1="30" x2="44" y2="30"/>
          <path d="M18 22 H42 M18 38 H42"/>
        </g>
      </svg>
      <span class="label">www.coastlinespine.example</span>
    </div>

    <div class="contact-item contact-mail">
      <svg class="icon" viewBox="0 0 60 60" aria-hidden="true">
        <circle cx="30" cy="30" r="29" fill="var(--ink)"/>
        <rect x="16" y="20" width="28" height="20" fill="var(--lime)"/>
        <path d="M16 20 L30 32 L44 20 M16 40 L26 29 M44 40 L34 29" fill="none" stroke="var(--ink)" stroke-width="1.8"/>
      </svg>
      <span class="label">hello@coastlinespine.example</span>
    </div>

    <div class="contact-item contact-phone">
      <svg class="icon" viewBox="0 0 60 60" aria-hidden="true">
        <circle cx="30" cy="30" r="29" fill="var(--ink)"/>
        <path d="M22 15 C19 16 17 19 18 24 C20 33 27 41 36 43 C40 44 43 42 45 39 L39 33 L34 36 C30 34 26 30 24 26 L27 21 Z" fill="var(--lime)"/>
      </svg>
      <span class="label">(000)555-014-278</span>
    </div>

    <div class="services">
      <h3>Our Services</h3>
      <ul>
        <li>Stem Cell Allograft · PRP</li>
        <li>Prolotherapy · Trigger Point</li>
        <li>Chiropractic · Rehab</li>
      </ul>
    </div>
  </section>

  <section class="cover-panel">
    <div class="brand-mark">
      <span class="brand-square"></span>
      <span class="brand-name">Coastline<br>Spine &amp; Joint</span>
    </div>
    <h1>Joint Arthritis<br>&amp; Muscle Pain<br>&amp; Injuries</h1>
    <p class="intro">The team at Coastline Spine &amp; Joint offers minimally invasive Regenerative Medicine techniques to help you recover from Chronic Pain</p>
  </section>

</div>
</body>
</html>
```